Web design for TRADEBACKS. A forex rebate platform website

I need a complete design for a forex rebate website called TRADEBACKS. The website will include the following pages:

- Homepage
- Broker Listing Page
- Broker Rebate Detail Page

Please review the attached file for detailed requirements and the content that needs to be designed.

Number of Pages Required

3 page

```html
<!DOCTYPE html>
<html lang="en">
<head>
<meta charset="utf-8">
<title>Tradebacks — Forex Rebates</title>
<link href="https://fonts.googleapis.com/css2?family=Inter:wght@400;500;600;700&display=swap" rel="stylesheet">
<style>
:root{
  --ink:#101c36;
  --navy:#1a2a55;
  --navy-2:#233566;
  --blue:#0b5cff;
  --bar:#6f95e8;
  --pale:#eef3fc;
  --line:#c9cfdb;
  --muted:#4a5470;
  --white:#ffffff;
  --black:#000000;
}
*{margin:0;padding:0;box-sizing:border-box}
html,body{width:1200px;height:1200px;overflow:hidden;background:var(--black)}
body{font-family:"Inter",sans-serif;color:var(--ink);position:relative}
.abs{position:absolute}
.sheet{position:absolute;background:var(--white)}
.c{text-align:center}
.h2{font-weight:600;font-size:15.5px;color:var(--ink);white-space:nowrap;transform:translateX(-50%)}
.blue{color:var(--blue)}

/* header */
.logo{font-weight:600;font-size:8.5px;color:var(--blue)}
.nav{font-size:5px;color:#333;top:25px}
.btn{display:flex;align-items:center;justify-content:center;border-radius:3px;font-size:5px}
.btn-out{border:0.6px solid var(--blue);color:var(--blue);background:#fff}
.btn-fill{background:var(--blue);color:#fff}

/* hero */
.hero{left:61px;top:43px;width:479px;height:202px;background:linear-gradient(100deg,#18284f,#243869 70%,#1d2d59)}
.hero-title{left:81px;top:66px;font-size:16.5px;line-height:19.5px;font-weight:500;color:#fff}
.hero-text{left:81px;top:132px;width:160px;font-size:8.6px;line-height:11px;color:#fff}
.hero-btn{top:193px;height:17px;font-size:6.2px;border-radius:2px}
.dash{left:312px;top:64px;width:208px;height:147px;border-radius:3px;overflow:hidden}
.panel{background:var(--navy-2);border-radius:2px}
.linked{position:absolute;top:22px;font-size:6px;font-weight:500;color:#fff}

/* stats */
.stats{left:81px;top:229px;width:439px;height:43px;background:#fff;border-radius:4px;box-shadow:0 2px 5px rgba(0,0,0,.15);display:flex;align-items:center}
.stat{flex:1;display:flex;align-items:center;gap:6px;padding-left:22px;border-right:0.8px solid var(--line);height:26px}
.stat:last-child{border-right:none}
.stat-ico{width:20px;height:15px;background:#dce6fb;border-radius:2px;display:flex;align-items:center;justify-content:center;color:var(--blue);font-size:7px}
.stat b{display:block;color:var(--blue);font-weight:500;font-size:9px;line-height:10px}
.stat span{display:block;font-size:6.2px;line-height:8px;color:var(--muted)}

/* how cards */
.how{top:371px;width:137px;height:129px;background:var(--pale);border-radius:8px}
.ribbon{position:absolute;left:54px;top:0;width:29px;height:28px;background:var(--navy);clip-path:polygon(0 0,100% 0,100% 100%,50% 82%,0 100%);color:#fff;font-weight:600;font-size:10px;text-align:center;padding-top:3px}
.how-art{position:absolute;left:48px;width:41px;height:38px;background:linear-gradient(#dbe5f8,#c7d6f4);border-radius:4px}
.how h3{position:absolute;left:0;right:0;text-align:center;font-size:10.5px;font-weight:600}
.how p{position:absolute;left:14px;right:14px;text-align:center;font-size:4.6px;line-height:5.8px}

/* brokers */
.broker{width:104px;border:0.7px solid #333;border-radius:3px;background:#fff}
.b-logo{position:absolute;left:15px;top:12px;font-size:8px;font-weight:600;color:var(--ink)}
.b-row{position:absolute;left:15px;font-size:4.8px;color:var(--ink)}
.b-max{position:absolute;left:64px;font-size:4.8px;color:var(--blue)}
.b-btn{position:absolute;left:16px;width:71px;height:14px;background:var(--blue);color:#fff;font-size:5px;border-radius:2px;display:flex;align-items:center;justify-content:center}

/* calculator */
.calc{left:288px;top:782px;width:227px;height:110px;background:var(--pale)}
.field{position:absolute;height:12px;background:#fff;font-size:5px;display:flex;align-items:center;padding:0 4px}

/* why */
.why{top:948px;width:101px;height:52px;background:var(--pale);border-radius:6px}
.why-ico{position:absolute;left:9px;top:18px;width:14px;height:14px;border:0.8px solid #555;border-radius:3px}
.why h4{position:absolute;left:30px;top:14px;font-size:7.2px;font-weight:600;white-space:nowrap}
.why p{position:absolute;left:30px;top:25px;width:66px;font-size:5.2px;line-height:6.4px}

/* right column */
.strip{left:572px;top:27px;width:425px;height:70px;border:0.7px solid #999;border-radius:8px;background:#fff}
.person{position:absolute;top:22px;font-size:6.8px}
.avatar{position:absolute;width:16px;height:16px;border-radius:50%;background:linear-gradient(#b7a597,#6a5b52)}
.person small{display:block;font-size:5.3px;color:var(--muted)}
.person .ago{display:block;font-size:2.6px;color:var(--muted)}
.step{left:572px;width:266px;height:70px;border:0.7px solid #999;border-radius:6px;background:#fff}
.step-badge{position:absolute;left:10px;top:19px;width:30px;height:32px;background:var(--pale);color:var(--blue);font-size:7.5px;font-weight:500;display:flex;align-items:center;justify-content:center;border-radius:2px}
.step h4{position:absolute;left:47px;top:22px;font-size:10px;font-weight:500}
.step p{position:absolute;left:47px;top:40px;width:180px;font-size:7.2px;line-height:9.5px}
.payout{left:853px;top:165px;width:149px;height:228px;border:2px solid var(--navy);border-radius:6px;background:#fff}
.pay{position:absolute;left:5px;width:118px;height:32px;background:var(--pale);border-radius:2px}
.pay-tag{position:absolute;left:6px;top:8px;width:18px;height:16px;background:#d2daea;font-size:7px;font-weight:500;display:flex;align-items:center;justify-content:center}
.pay-name{position:absolute;left:27px;top:7px;font-size:5.5px;font-weight:600;color:var(--ink)}
.pay-time{position:absolute;left:27px;top:19px;font-size:4.8px;color:var(--muted)}
.pay-amt{position:absolute;right:5px;top:13px;font-size:7px;font-weight:600;color:var(--blue)}
.proof{left:578px;top:551px;width:622px;height:227px;background:var(--blue)}
.proof-card{left:612px;top:584px;width:288px;height:161px;background:#fff;display:flex;align-items:center;justify-content:center;font-size:31px;font-weight:600;color:var(--navy)}
</style>
</head>
<body>

<div class="sheet" style="left:0;top:102px;width:1200px;height:995px"></div>
<div class="sheet" style="left:61px;top:12px;width:481px;height:100px"></div>
<div class="sheet" style="left:543px;top:12px;width:480px;height:100px"></div>

<!-- header -->
<div class="abs logo" style="left:84px;top:23px">Tradebacks</div>
<div class="abs nav" style="left:181px">How it works</div>
<div class="abs nav" style="left:241px">Brokers</div>
<div class="abs nav" style="left:288px">About</div>
<div class="abs nav" style="left:331px">News</div>
<div class="abs nav" style="left:373px">EN ⌄</div>
<div class="abs btn btn-out" style="left:438px;top:22px;width:30px;height:13px">Log In</div>
<div class="abs btn btn-fill" style="left:477px;top:22px;width:44px;height:13px">Sign Up Free</div>

<!-- hero -->
<div class="abs hero" role="img" aria-label="Dark navy trading chart backdrop"></div>
<div class="abs hero-title"><span class="blue">FOREX</span> REBATES<br>MADE SIMPLE. UP TO<br>90% BACK.</div>
<div class="abs hero-text">Earn higher rebates from the world's leading forex brokers without affecting your spreads, commissions, or trading conditions.</div>
<div class="abs btn btn-fill hero-btn" style="left:81px;width:86px">Start Earning Rebates</div>
<div class="abs btn hero-btn" style="left:178px;width:77px;border:0.8px solid #fff;color:#fff">Compare Brokers</div>

<div class="abs dash">
  <div class="abs" style="left:0;top:0;width:208px;height:17px;background:#fff"></div>
  <div class="abs" style="left:14px;top:5px;font-size:3.2px;color:var(--blue)">Tradebacks</div>
  <div class="abs" style="left:63px;top:5px;font-size:6.3px;color:var(--blue);font-weight:500">Trader Dashboard</div>
  <div class="abs" style="left:177px;top:3px;width:9px;height:9px;border-radius:50%;background:var(--blue);color:#fff;font-size:4px;text-align:center;line-height:9px">D</div>
  <div class="abs" style="left:190px;top:5px;font-size:3.5px;color:var(--blue)">David</div>
  <div class="abs" style="left:0;top:17px;width:54px;height:130px;background:#fff"></div>
  <div class="abs" style="left:3px;top:16px;width:50px;height:12px;border:0.7px solid var(--blue);border-radius:2px;font-size:4.8px;padding:3px 0 0 18px">Dashboard</div>
  <div class="abs" style="left:19px;top:37px;font-size:4.8px;line-height:14.5px">My Brokers<br>Payouts<br>Live Feed<br>Settings</div>
  <div class="abs" style="left:54px;top:17px;width:154px;height:130px;background:#16244a"></div>
  <div class="abs panel" style="left:59px;top:22px;width:146px;height:54px">
    <div class="abs" style="left:7px;top:5px;font-size:4.8px;color:#fff">Total Rebates Accrued</div>
    <div class="abs" style="left:7px;top:14px;font-size:8px;color:#fff;font-weight:500">$234,435.65</div>
    <div class="abs" style="left:7px;top:44px;font-size:3.4px;color:#ccd">Updated Real time</div>
    <div class="abs" style="left:119px;top:4px;font-size:3.4px;color:#fff">87.87%</div>
    <svg class="abs" style="left:78px;top:14px" width="50" height="36" viewBox="0 0 50 36">
      <line x1="0" y1="35" x2="50" y2="35" stroke="#5a6a92" stroke-width="0.6"/>
      <rect x="4" y="26" width="6" height="9" fill="var(--bar)"/>
      <rect x="14" y="20" width="6" height="15" fill="var(--bar)"/>
      <rect x="24" y="14" width="6" height="21" fill="var(--bar)"/>
      <rect x="34" y="6" width="6" height="29" fill="var(--blue)"/>
    </svg>
  </div>
  <div class="abs panel" style="left:59px;top:81px;width:146px;height:66px">
    <div class="abs" style="left:7px;top:6px;font-size:4.8px;color:#fff">Linked Brokers</div>
    <div class="linked" style="left:8px">Halden</div>
    <div class="linked" style="left:56px">Corvane</div>
    <div class="linked" style="left:104px">Norvik</div>
    <div class="abs" style="left:16px;top:43px;font-size:4.8px;color:#fff">Account #</div>
    <div class="abs" style="left:58px;top:43px;font-size:4.8px;color:#fff">Status</div>
    <div class="abs" style="left:93px;top:43px;font-size:4.8px;color:#fff">Rebate Plan ⌄</div>
    <div class="abs" style="left:16px;top:54px;width:112px;height:7px;border:0.5px solid #889;font-size:3.3px;color:#fff;line-height:6px">
      <span style="margin-left:7px">MT1234567</span><span style="margin-left:22px;color:var(--blue);font-size:4px">Active</span><span style="margin-left:22px">Loss Rab</span></div>
  </div>
</div>

<!-- stats -->
<div class="abs stats">
  <div class="stat"><div class="stat-ico">$</div><div><b>$7.5M+</b><span>Rebates Paid</span></div></div>
  <div class="stat"><div class="stat-ico">◎</div><div><b>15,000+</b><span>Active Traders</span></div></div>
  <div class="stat"><div class="stat-ico">⟳</div><div><b>40+</b><span>Supported Brokers</span></div></div>
  <div class="stat"><div class="stat-ico">◉</div><div><b>Daily</b><span>Payout Frequency</span></div></div>
</div>

<!-- what is -->
<div class="abs h2" style="left:299px;top:306px">What is a Forex Rebate?</div>
<div class="abs c" style="left:120px;top:330px;width:360px;font-size:8.7px;line-height:11px">Every trade generates spread or commission fees. Instead of letting those costs add up, Tradebacks returns a significant portion back to you as cashback rebates.</div>

<div class="abs how" style="left:83px">
  <div class="ribbon">1</div>
  <div class="how-art" style="top:34px" role="img" aria-label="Line illustration of a trader"></div>
  <h3 style="top:81px">Trade As Usual</h3>
  <p style="top:96px">Keep trading with your broker normally. No changes to your platform, spreads, or execution.</p>
</div>
<div class="abs how" style="left:230px">
  <div class="ribbon">2</div>
  <div class="how-art" style="top:37px;height:30px" role="img" aria-label="Line illustration of a payment card"></div>
  <h3 style="top:77px">Broker Pays Us</h3>
  <p style="top:92px">Your broker pays Tradebacks a commission for introducing you as a client.</p>
</div>
<div class="abs how" style="left:378px">
  <div class="ribbon">3</div>
  <div class="how-art" style="top:34px;height:30px" role="img" aria-label="Line illustration of a money bag"></div>
  <h3 style="top:74px">Get Cashback</h3>
  <p style="top:89px">We share up to $50 per lot back with you through daily rebate payments.</p>
</div>

<!-- brokers -->
<div class="abs h2" style="left:298px;top:529px">Trusted Brokers</div>

<div class="abs broker" style="left:81px;top:558px;height:79px">
  <div class="b-logo">Halden</div>
  <div class="b-row" style="top:34px">Mex Rebates</div><div class="b-max" style="top:34px">90% Max</div>
  <div class="b-row" style="top:44px">Account Types</div>
  <div class="b-btn" style="top:55px">Quick View</div>
</div>
<div class="abs broker" style="left:193px;top:558px;height:79px">
  <div class="b-logo" style="top:11px">Norvik</div>
  <div class="b-row" style="top:32px">Mer Rebstes</div><div class="b-max" style="top:32px">Max 80%</div>
  <div class="b-row" style="top:42px">Account Types</div>
  <div class="b-btn" style="top:53px">Quick View</div>
</div>
<div class="abs broker" style="left:305px;top:558px;height:79px">
  <div class="b-logo">Brightlane</div>
  <div class="b-row" style="top:34px">Mex Rebates</div><div class="b-max" style="top:34px">90% Max</div>
  <div class="b-row" style="top:44px">Account Types</div>
  <div class="b-btn" style="top:55px">Quick View</div>
</div>
<div class="abs broker" style="left:417px;top:558px;height:167px">
  <div class="b-logo" style="top:56px;font-size:10px">Quarry</div>
  <div class="b-row" style="top:76px;left:16px">Mex Rebates</div><div class="b-max" style="top:76px">90% Max</div>
  <div class="b-row" style="top:86px;left:16px">Account Types</div>
  <div class="b-btn" style="top:97px">Quick View</div>
</div>
<div class="abs broker" style="left:81px;top:646px;height:79px">
  <div class="b-logo">Pellham</div>
  <div class="b-row" style="top:34px">Mex Rebates</div><div class="b-max" style="top:34px">90% Max</div>
  <div class="b-row" style="top:44px">Account Types</div>
  <div class="b-btn" style="top:55px">Quick View</div>
</div>
<div class="abs broker" style="left:193px;top:646px;height:79px">
  <div class="b-logo" style="top:11px">Ostwind</div>
  <div class="b-row" style="top:32px">Mer Rebstes</div><div class="b-max" style="top:32px">Max 80%</div>
  <div class="b-row" style="top:42px">Account Types</div>
  <div class="b-btn" style="top:53px">Quick View</div>
</div>
<div class="abs broker" style="left:305px;top:646px;height:79px">
  <div class="b-logo">Larkfield</div>
  <div class="b-row" style="top:34px">Mex Rebates</div><div class="b-max" style="top:34px">90% Max</div>
  <div class="b-row" style="top:44px">Account Types</div>
  <div class="b-btn" style="top:55px">Quick View</div>
</div>

<!-- calculator -->
<div class="abs h2" style="left:292px;top:754px">Rebate Calculator</div>
<div class="abs" style="left:81px;top:806px;width:195px;font-size:8.7px;line-height:11px">Earnings will very much depend on the rebate rate of your broker, the instruments you trade as well as the volume of your trades.</div>
<div class="abs" style="left:81px;top:844px;width:195px;font-size:10.4px;line-height:13px;font-weight:500">Use the calculator below to roughly estimate yourearnings.</div>
<div class="abs calc">
  <div class="abs" style="left:8px;top:5px;font-size:10px;color:var(--blue);font-weight:500">Cashback Calculator</div>
  <div class="abs" style="left:8px;top:20px;font-size:8.8px">Estimate your Cashback</div>
  <div class="abs" style="left:8px;top:42px;font-size:4.6px">Select Broker</div>
  <div class="abs" style="left:88px;top:43px;font-size:4.6px">Let's Trader every Month</div>
  <div class="field" style="left:8px;top:53px;width:74px;justify-content:space-between"><span>Norvik</span><span>⌄</span></div>
  <div class="field" style="left:88px;top:53px;width:74px;justify-content:space-between"><span>10</span><span>lets</span></div>
  <div class="abs" style="left:8px;top:75px;font-size:6px">Estimated Cashback</div>
  <div class="abs" style="left:8px;top:85px;font-size:6.8px;line-height:8px;color:var(--blue);font-weight:500">$653,323.45/<br>Month</div>
  <div class="abs btn btn-fill" style="left:78px;top:90px;width:71px;height:15px">Start Saving Today</div>
  <div class="abs" style="left:168px;top:24px;width:40px;height:58px;border-radius:6px;background:linear-gradient(#d7dde9,#bfc6d4);transform:rotate(-22deg)" role="img" aria-label="Calculator illustration"></div>
</div>

<!-- why -->
<div class="abs h2" style="left:291px;top:920px">Why Choose Tradebacks</div>
<div class="abs why" style="left:81px"><div class="why-ico"></div><h4>Real-Time Reports</h4><p>View your earnings in real-time.</p></div>
<div class="abs why" style="left:194px"><div class="why-ico" style="border-radius:50%"></div><h4 style="top:13px">Highest Rebate Rates</h4><p style="top:24px">We pay the best rebate rates.</p></div>
<div class="abs why" style="left:307px"><div class="why-ico"></div><h4>Fast Payouts</h4><p>Get your rebates quickly and securely.</p></div>
<div class="abs why" style="left:420px"><div class="why-ico"></div><h4 style="top:11px">Awesome Support</h4><p style="top:22px">Get answers for any query you may have on time.</p></div>

<div class="abs h2" style="left:282px;top:1027px">Live Rebates Feed</div>

<!-- right: testimonials -->
<div class="abs strip">
  <div class="avatar" style="left:23px;top:22px" role="img" aria-label="Trader portrait"></div>
  <div class="person" style="left:43px;top:25px">Indonesian<small>Received $245.80</small><span class="ago">2 Minutes ago</span></div>
  <div class="abs" style="left:23px;top:41px;font-size:6.8px">John</div>
  <div class="avatar" style="left:179px;top:21px" role="img" aria-label="Trader portrait"></div>
  <div class="person" style="left:203px;top:24px">Thailand<small>Received $412.30</small><span class="ago">5 Minutes ago</span></div>
  <div class="abs" style="left:174px;top:41px;font-size:6.8px">Micheal</div>
  <div class="avatar" style="left:335px;top:21px" role="img" aria-label="Trader portrait"></div>
  <div class="person" style="left:356px;top:24px">Nigeria<small>Received $186.20</small><span class="ago">7 Minutes ago</span></div>
  <div class="abs" style="left:334px;top:41px;font-size:6.8px">David</div>
</div>

<div class="abs h2" style="left:781px;top:125px">Earn Forex Cashback in 3 Easy Steps</div>
<div class="abs step" style="top:157px"><div class="step-badge">Step 1</div><h4>Create Your Account</h4><p>Sign up for free and activate your cashback profile.</p></div>
<div class="abs step" style="top:238px"><div class="step-badge">Step 2</div><h4>Link Your Trading Account</h4><p>Open a new account or connect an existing account with a partner broker.</p></div>
<div class="abs step" style="top:319px"><div class="step-badge">Step 3</div><h4>Receive Cashback</h4><p>Earn automatic rebate payments on every eligible trade.</p></div>

<div class="abs payout">
  <div class="abs" style="left:10px;top:12px;font-size:10px;font-weight:500;color:var(--blue)">Recent Payout</div>
  <div class="pay" style="top:33px"><div class="pay-tag">OW</div><div class="pay-name">Ostwind</div><div class="pay-time">9:00 to 10:00 AM</div><div class="pay-amt">+$16.80</div></div>
  <div class="pay" style="top:75px"><div class="pay-tag">LF</div><div class="pay-name">Larkfield</div><div class="pay-time">9:00 to 10:00 AM</div><div class="pay-amt">+$56.80</div></div>
  <div class="pay" style="top:117px"><div class="pay-tag">PH</div><div class="pay-name">Pellham</div><div class="pay-time">9:00 to 10:00 AM</div><div class="pay-amt">+$17.80</div></div>
  <div class="pay" style="top:160px"><div class="pay-tag">NV</div><div class="pay-name">Norvik</div><div class="pay-time">9:00 to 10:00 AM</div><div class="pay-amt">+$16.30</div></div>
</div>

<div class="abs h2" style="left:781px;top:431px">Real Payout Proofs</div>
<div class="abs" style="left:781px;top:462px;transform:translateX(-50%);white-space:nowrap;font-size:7.6px;font-weight:500">Every screenshot below is a genuine payment received by our traders.</div>

<div class="abs proof"></div>
<div class="abs proof-card">Tradebacks</div>

</body>
</html>
```